Luxury Wine Label for New Startup Winery

We need a wine label for our new winery startup. We have worked with a local designer but do not feel the resulting label / logo have the elevation required to present our brand as a luxury wine. Our winery is called "Harrowgate Vineyards" and we are focused on extremely high quality hand crafted artisan and estate wines from the Pacific Northwest.
We would like to see designs that utilize a tree line, or other imagery that represents the "Harrowgate" part of our company name. Another interesting feature could be wood grain.
A logo will be required based on your design so please design with this in mind:
This logo should be consistent with the wine bottle label design, and should be representative of our high end exclusive wine while giving a sense of place (Oregon/ Pacific Northwest.)
I will supply an image of the design we received from our local designer, PLEASE NOTE: in general we do like wood grain and tree line concepts but feel the execution was poorly done.
ATTN: Logo design should be suitable for use on: Bottles (Red wine/rose/white wine), Bussiness cards, vehicle signage, business signage, etc
P.S.:
If you have a design that is not outside the box we are still interested in seeing it.
Label is for a burgundy style bottle with a label height of 3.5 - 4" and a width of 3.5-4"
any label <= 4"x4" and >=3.5"x3.5" will be acceptable:
HOWEVER Width should be greater than or equal to height due to the bottle format
Target Market(s)
Wine enthusiasts with adequate discretionary budgets to afford $100 bottles of wine.
Industry/Entity Type
Wine / Winery
Requirements
Must have
- A sense of luxury, a feel of exclusivity, and a theme consistent with our product and brand name
Nice to have
- Tree line, wood grain or other wood themes. Serif fonts
Should not have
- anything cheesy, off topic, hard to read script fonts or anything that makes the label hard to read from a few feet away or too busy

```html
<!DOCTYPE html>
<html lang="en">
<head>
<meta charset="UTF-8">
<title>Harrowgate Vineyards – 2024 Rosé Label</title>
<link rel="stylesheet" href="https://fonts.googleapis.com/css2?family=Cinzel:wght@400;500&family=Playfair+Display:ital,wght@1,600&display=swap">
<style>
  :root {
    --backdrop: #eef4f7;
    --label-paper: #fffdf8;
    --ink-dark: #1f1a16;
    --accent-red: #e0231c;
    --contour-light: #f8cfa6;
    --contour-mid: #ee7434;
    --contour-deep: #c8321a;
    --contour-dark: #6e140a;
  }
  * { margin: 0; padding: 0; box-sizing: border-box; }
  html, body {
    width: 774px;
    height: 1200px;
    overflow: hidden;
    background: var(--backdrop);
  }
  .canvas {
    position: relative;
    width: 774px;
    height: 1200px;
  }
  .wine-label {
    position: absolute;
    left: 47px;
    top: 270px;
    width: 680px;
    height: 660px;
    background: var(--label-paper);
    overflow: hidden;
  }
  .brand-name {
    position: absolute;
    top: 50px;
    left: 0;
    width: 100%;
    text-align: center;
    font-family: "Cinzel", serif;
    font-weight: 400;
    font-size: 58px;
    line-height: 1;
    letter-spacing: 1px;
    color: var(--ink-dark);
  }
  .brand-sub {
    position: absolute;
    top: 126px;
    left: 0;
    width: 100%;
    text-align: center;
    font-family: "Cinzel", serif;
    font-weight: 400;
    font-size: 46px;
    line-height: 1;
    letter-spacing: 7px;
    color: var(--ink-dark);
  }
  .wine-designation {
    position: absolute;
    top: 216px;
    left: 0;
    width: 100%;
    text-align: center;
    line-height: 1;
  }
  .vintage {
    font-family: "Playfair Display", serif;
    font-style: italic;
    font-weight: 600;
    font-size: 22px;
    color: var(--ink-dark);
    margin-right: 8px;
    vertical-align: 12px;
  }
  .varietal {
    font-family: "Cinzel", serif;
    font-weight: 400;
    font-size: 40px;
    color: var(--accent-red);
  }
  .terrain-art {
    position: absolute;
    left: 0;
    top: 296px;
    width: 680px;
    height: 364px;
    background:
      linear-gradient(180deg,
        var(--label-paper) 0%,
        rgba(255,253,248,0) 30%),
      linear-gradient(100deg,
        var(--contour-light) 0%,
        var(--contour-mid) 45%,
        var(--contour-deep) 75%,
        var(--contour-dark) 100%);
    opacity: 0.42;
  }
</style>
</head>
<body>
  <main class="canvas">
    <section class="wine-label">
      <h1 class="brand-name">HARROWGATE</h1>
      <p class="brand-sub">VINEYARDS</p>
      <p class="wine-designation">
        <span class="vintage">2024</span><span class="varietal">ROSE</span>
      </p>
      <div class="terrain-art" role="img" aria-label="Topographic contour-line illustration of rolling vineyard hills in warm peach, orange and deep red lines"></div>
    </section>
  </main>
</body>
</html>
```